Lotus Bridge Trust Flyer Design Project

We need an A5 one sided flyer design for a registered UK Charity Lotus Bridge Trust (Reg no 2263517). We support disadvantaged children in Goa, India. Our main project is Kestrel Lodge near Mapusa in North Goa. From their base at Kestrel Lodge they support around 150 children and provide uniforms and school bags to many more children. In addition to promoting this work we want to encourage people to visit them

You can read more about our work, logo and the colour scheme we use at www.lotusbridgetrust.org
We have a facebook page Lotus Bridge Trust

Our main project is Kestrel Lodge near Mapusa, Goa, India

Target Market(s)

simply those who might support our work

Industry/Entity Type

School

Requirements
Must have
• At least one photograph of children supported by Kestrel Lodge but these should be uplifting not showing children in distress. These must showcase our work i.e education, food and health

A photograph of Kestrel Lodge and its address and contact details. An invitation to visit Kestrel Lodge by contacting kestrelfund@quillpost.example or calling +917340528193

Our website, UK address facebook page and contact details. -info@lotusbridgetrust.org

It must be stated that we are a registered charity in England and Wales Reg. No 2263517

The following words must be included.
"We are a UK registered charity supporting disadvantaged children and young people in Goa, India regardless of their religion, class, caste or gender. The charity is administered entirely voluntarily which means that more of your money is available to fund our projects in Goa.

We aim to break the cycle of poverty and believe that education can transform lives.We focus on educational support but we know good health and nutrition are all essential to a child's chances of success at school and we therefore also provide meals and healthcare too.We support projects in Mapusa, Colva and Chimbel and we also fund a school uniform and school bag scheme which provides hundreds of uniforms and bags each year. Our main partner is The Kestrel Lodge Fund based at Kestrel Lodge near Mapusa.
You can read more about our work at www.lotusbridgetrust.org . However, if you are in Goa we welcome visits to Kestrel Lodge.
Nice to have
• A few inspiring photos of children

We would have liked to attach more but were limited to uploading 5
Should not have
• Photos of children in distress

```html
<!DOCTYPE html>
<html lang="en">
<head>
<meta charset="utf-8">
<title>Lotus Bridge Trust – Flyer</title>
<link href="https://fonts.googleapis.com/css2?family=Open+Sans:ital,wght@0,400;0,600;1,400;1,600&display=swap" rel="stylesheet">
<style>
  :root {
    --crimson: #c2163f;
    --crimson-deep: #8e1030;
    --pink: #e8306a;
    --white: #ffffff;
    --ink: #3a3a3a;
    --muted: #555555;
    --sky: #1aa3e0;
    --logo-blue: #2f7fc1;
    --backdrop: #e9e9ec;
  }
  * { box-sizing: border-box; margin: 0; padding: 0; }
  html, body { width: 1200px; height: 1000px; overflow: hidden; }
  body {
    background: var(--backdrop);
    font-family: "Open Sans", Arial, sans-serif;
    color: var(--ink);
  }
  .flyer {
    position: absolute;
    left: 50px; top: 110px;
    width: 1100px; height: 780px;
    background: var(--white);
    overflow: hidden;
    box-shadow: 0 6px 24px rgba(0,0,0,.18);
  }
  .flyer__backdrop { position: absolute; inset: 0; }
  .photo { position: absolute; }
  .photo--lodge {
    left: 0; top: 0; width: 430px; height: 245px;
    background: linear-gradient(135deg, #9fb8d8 0%, #3b66b0 35%, #d9c2a6 60%, #5f8a3c 100%);
    border-radius: 0 0 60% 0 / 0 0 40% 0;
  }
  .photo--girl {
    left: 385px; top: 335px; width: 320px; height: 320px;
    border-radius: 50%;
    background: radial-gradient(circle at 45% 40%, #c79a7a 0%, #8d2a40 55%, #6a1a2c 100%);
    border: 6px solid var(--white);
  }
  .photo--boy {
    left: 680px; top: 300px; width: 420px; height: 480px;
    background: radial-gradient(circle at 45% 45%, #b9825e 0%, #8a5a3e 45%, #cfd6d0 85%);
    border-radius: 60% 0 0 45% / 35% 0 0 40%;
    border-top: 6px solid var(--white);
    border-left: 6px solid var(--white);
  }
  .intro {
    position: absolute;
    left: 462px; top: 22px; width: 620px; height: 268px;
    background: var(--white);
    border-radius: 30px;
    padding: 14px 158px 12px 24px;
    font-style: italic;
    font-size: 10.8px;
    line-height: 1.36;
  }
  .intro p { text-indent: 20px; }
  .intro p + p { margin-top: 3px; }
  .brand {
    position: absolute;
    right: 16px; top: 40px; width: 134px;
    text-align: center;
  }
  .brand__mark {
    width: 56px; height: 56px; border-radius: 50%;
    background: var(--logo-blue);
    margin: 0 auto 10px;
  }
  .brand__name {
    font-weight: 600; font-size: 16px; line-height: 1.2;
    color: var(--logo-blue);
  }
  .contact {
    position: absolute;
    left: 36px; top: 256px; width: 316px; height: 362px;
    background: var(--white);
    border-radius: 28px;
    box-shadow: 0 4px 14px rgba(0,0,0,.16);
    padding: 12px 12px;
    text-align: center;
    font-style: italic;
    font-size: 11.6px;
    line-height: 1.38;
  }
  .contact__heading { color: var(--sky); font-weight: 600; }
  .contact__block + .contact__block { margin-top: 4px; }
  .contact__note { color: var(--sky); margin-top: 6px; }
  .cta {
    position: absolute;
    left: 66px; top: 640px; width: 276px; height: 84px;
    border-radius: 40px;
    background: linear-gradient(180deg, var(--crimson) 0%, var(--crimson-deep) 100%);
    color: var(--white);
    text-align: center;
    font-style: italic; font-weight: 600;
    font-size: 16px; line-height: 1.35;
    padding-top: 19px;
  }
  .bubble {
    position: absolute;
    left: 585px; top: 570px; width: 225px; height: 130px;
    background: var(--white);
    border-radius: 34px;
    padding: 18px 14px;
    text-align: center;
    font-style: italic; font-size: 14.5px; line-height: 1.35;
    color: var(--muted);
  }
  .bubble__tail { position: absolute; left: -34px; top: 88px; }
</style>
</head>
<body>
  <main class="flyer">
    <svg class="flyer__backdrop" width="1100" height="780" viewBox="0 0 1100 780" aria-hidden="true">
      <defs>
        <linearGradient id="band" x1="0" y1="0" x2="1" y2="1">
          <stop offset="0" stop-color="#a5123a"/>
          <stop offset="0.5" stop-color="#c2163f"/>
          <stop offset="1" stop-color="#d9245a"/>
        </linearGradient>
      </defs>
      <path d="M410 0 L1100 0 L1100 780 L300 780 C340 600 380 430 460 280 C510 190 470 70 410 0 Z" fill="url(#band)"/>
      <path d="M320 780 C350 710 375 660 405 625 L470 660 C440 700 425 745 415 780 Z" fill="#e8306a" opacity="0.8"/>
      <path d="M1000 0 L1100 0 L1100 230 C1070 150 1040 70 1000 0 Z" fill="#f07a3a"/>
    </svg>

    <div class="photo photo--lodge" role="img" aria-label="Photograph of Kestrel Lodge, a blue and cream colonial house with a tiled roof and garden"></div>

    <section class="intro">
      <p>We are a UK registered charity supporting disadvantaged children and young people in Goa, India regardless of their religion, class, caste or gender. The charity is administered entirely voluntarily which means that more of your money is available to fund our projects in Goa.</p>
      <p>We aim to break the cycle of poverty and believe that education can transform lives. We focus on educational support but we know good health and nutrition are all essential to a child's chances of success at school and we therefore also provide meals and healthcare too. We support projects in Mapusa, Colva and Chimbel and we also fund a school uniform and school bag scheme which provides hundreds of uniforms and bags each year. Our main partner is The Kestrel Lodge Fund based at Kestrel Lodge near Mapusa.</p>
      <p>You can read more about our work at www.lotusbridgetrust.org. However, if you are in Goa we welcome visits to Kestrel Lodge.</p>
      <div class="brand">
        <div class="brand__mark"></div>
        <div class="brand__name">Lotus Bridge Trust</div>
      </div>
    </section>

    <section class="contact">
      <div class="contact__block">
        <p class="contact__heading">We'd love to see you<br>at Kestrel Lodge!</p>
        <p>Please call us on 0091 7340 528 193<br>or email kestrelfund@quillpost.example<br>and arrange a visit to our house!</p>
      </div>
      <div class="contact__block">
        <p class="contact__heading">Where we are</p>
        <p>Kestrel Lodge, House Number 62/7,<br>Near Sunrise Clinic, Karaswada, Mapusa,<br>Bardez, Goa - 403526 INDIA</p>
      </div>
      <div class="contact__block">
        <p class="contact__heading">UK office</p>
        <p>14 Willow Row, Harbury CV33 9XY<br>info@lotusbridgetrust.org<br>Facebook: Lotus Bridge Trust</p>
      </div>
      <p class="contact__note">We are a registered charity in<br>England and Wales<br>Reg. No 2263517</p>
    </section>

    <a class="cta">Visit our site<br>www.lotusbridgetrust.org</a>

    <div class="photo photo--girl" role="img" aria-label="Photograph of a smiling schoolgirl in a maroon uniform writing at her desk"></div>
    <div class="photo photo--boy" role="img" aria-label="Close-up photograph of a smiling schoolboy"></div>

    <div class="bubble">
      <svg class="bubble__tail" width="50" height="40" viewBox="0 0 50 40" aria-hidden="true">
        <path d="M50 0 L0 34 L50 30 Z" fill="#ffffff"/>
      </svg>
      We support<br>around 150 children and provide uniforms and school bags to many more children.
    </div>
  </main>
</body>
</html>
```